Velmora Steam Cleaning website for demos

Velmora Steam Cleaning is a business that provides commercial cleaning services utilizing steam vapor, which offers the most effective and ecologically friendly method of cleaning today. We need a website to advertise our services, and needs to incorporate spaces to show video demonstrations on how the cleaning machine works.

Target Market(s)

The potential market for this business are hotels, motels, restaurants, hospitals, fast food facilities, nursing homes, day care centers, schools, country clubs, churches, office and apartment buildings, malls, movie theaters, super markets, airports, parks, and any other facility.

Industry/Entity Type

Business

Coding

Coded - Design and coding required

Number of Pages Required

3 page

Colors
add136
9bcb3c
34a6d7
3176b5
edf8f6

Requirements
Must have
• Areas for videos that serve as demonstrations of our services

```html
<!DOCTYPE html>
<html lang="en">
<head>
<meta charset="utf-8">
<title>Velmora Steam Cleaning</title>
<link rel="stylesheet" href="https://fonts.googleapis.com/css2?family=Open+Sans:ital,wght@0,300;0,400;0,600;0,700;1,400;1,600&display=swap">
<style>
:root{
  --green:#add136;
  --green-mid:#9bcb3c;
  --green-deep:#5e9a1e;
  --sky:#34a6d7;
  --blue:#3176b5;
  --navy:#1f4f86;
  --navy-deep:#183f6c;
  --mint:#edf8f6;
  --page:#e4e6e8;
  --ink:#444;
  --muted:#777;
  --white:#fff;
}
*{box-sizing:border-box;margin:0;padding:0}
html,body{width:1200px;height:2184px;overflow:hidden}
body{font-family:"Open Sans",Arial,sans-serif;color:var(--ink);background:var(--page);position:relative}
.site-header{position:absolute;top:0;left:0;width:1200px;height:150px;background:var(--white);z-index:2}
.brand{position:absolute;left:140px;top:22px;width:290px;height:100px;background:linear-gradient(180deg,#e8f4fb,#cfe6f4);border-radius:6px;display:flex;align-items:center;gap:14px;padding-left:20px}
.brand-dot{width:40px;height:40px;border-radius:50%;background:var(--sky);flex:none}
.brand-name{font-weight:700;font-size:22px;line-height:1.1;color:var(--blue)}
.top-phone{position:absolute;right:140px;top:14px;font-size:24px;font-weight:600;color:var(--blue);letter-spacing:1px}
.main-nav{position:absolute;right:130px;top:104px;display:flex;gap:34px;font-size:16px}
.main-nav a{color:var(--muted);text-decoration:none}
.main-nav a.active{color:var(--green-deep);font-weight:700}
.hero{position:absolute;top:150px;left:0;width:1200px;height:670px;background:linear-gradient(160deg,#9fb3c2 0%,#d6dee4 40%,#b8c6d0 70%,#7f96a8 100%)}
.hero-text{position:absolute;right:150px;top:340px;width:420px;text-align:center;font-style:italic;font-size:25px;line-height:1.35;color:var(--white);font-weight:600;text-shadow:0 2px 4px rgba(0,0,0,.35)}
.hero-text .eco{font-size:36px;color:var(--green)}
.panel{position:absolute;left:140px;top:820px;width:920px;height:1230px;background:var(--white)}
.welcome-title{position:absolute;top:14px;width:100%;text-align:center;font-size:24px;font-weight:600;color:var(--blue)}
.welcome-text{position:absolute;top:62px;left:60px;width:800px;text-align:center;font-size:16px;font-style:italic;line-height:1.6;color:var(--ink)}
.steam-banner{position:absolute;top:140px;left:20px;width:880px;height:380px;border-radius:4px;background:radial-gradient(circle at 50% 55%,#c7e85a 0%,#8cc63a 45%,#4d8f1d 100%)}
.banner-title{position:absolute;top:22px;left:300px;width:280px;padding:8px 0;text-align:center;background:rgba(255,255,255,.85);border-radius:20px;color:var(--green-deep);font-size:24px;font-style:italic;font-weight:600}
.banner-note{position:absolute;width:190px;text-align:center;font-size:14px;color:var(--white);font-weight:600;line-height:1.3;text-shadow:0 1px 2px rgba(0,0,0,.4)}
.lists{position:absolute;top:545px;left:20px;width:880px;display:flex;gap:30px}
.list-col{flex:1}
.list-head{display:flex;align-items:center;gap:12px;height:40px;padding-left:14px;border-radius:6px;background:linear-gradient(180deg,var(--sky),var(--blue));color:var(--white);font-size:20px;font-weight:700}
.list-head .drop{width:22px;height:22px;border-radius:50% 50% 50% 0;transform:rotate(-45deg);background:var(--green)}
.list-col ul{list-style:none;margin-top:12px}
.list-col li{display:flex;align-items:center;gap:12px;font-size:13px;color:var(--muted);height:27px;padding-left:10px;border-bottom:1px dotted #ddd}
.list-col li svg{flex:none}
.demo{position:absolute;top:920px;left:20px;width:880px;height:290px;background:linear-gradient(180deg,var(--green-mid),var(--green-deep));border-radius:4px}
.demo-title{position:absolute;left:40px;top:36px;font-size:40px;font-weight:300;line-height:1.1;color:var(--white)}
.demo-text{position:absolute;left:40px;top:150px;width:380px;font-size:13px;line-height:1.5;color:var(--white)}
.video{position:absolute;right:30px;top:30px;width:400px;height:230px;background:linear-gradient(135deg,#9fb1bd,#5d7382);border:4px solid var(--white)}
.video-bar{position:absolute;bottom:0;left:0;right:0;height:26px;background:rgba(0,0,0,.7)}
.video-bar span{position:absolute;left:40px;top:11px;width:260px;height:4px;background:#888}
.video-bar span::before{content:"";position:absolute;left:0;top:0;width:80px;height:4px;background:#d33}
.play{position:absolute;left:160px;top:70px}
.site-footer{position:absolute;top:2050px;left:0;width:1200px;height:134px;background:linear-gradient(180deg,var(--blue),var(--navy))}
.foot-col{position:absolute;top:10px;color:var(--white)}
.foot-col h3{font-size:15px;font-weight:700;margin-bottom:6px;line-height:1.4}
.quick{left:160px;width:300px}
.quick ul{list-style:none;display:grid;grid-template-columns:140px 140px;row-gap:5px;font-size:12px;line-height:1.4}
.contact{left:465px;width:300px;font-size:12px;line-height:1.4}
.contact p{display:flex;align-items:center;gap:8px;margin-bottom:4px}
.contact .phone{font-size:16px;font-weight:600}
.foot-brand{position:absolute;left:800px;top:16px;display:flex;align-items:center;gap:12px}
.foot-brand .brand-dot{background:rgba(255,255,255,.35)}
.foot-brand span{color:var(--white);font-size:20px;font-weight:700;line-height:1.1}
.socials{position:absolute;left:880px;top:72px;display:flex;gap:12px}
.socials i{width:30px;height:30px;border-radius:5px;background:var(--sky);display:block}
.copy-bar{position:absolute;left:0;bottom:0;width:1200px;height:24px;background:var(--navy-deep)}
.copy{position:absolute;left:160px;top:5px;font-size:11px;line-height:14px;color:#cfe0f0}
</style>
</head>
<body>
<header class="site-header">
  <div class="brand"><span class="brand-dot"></span><span class="brand-name">Velmora<br>Steam Cleaning</span></div>
  <div class="top-phone">123 456 7890</div>
  <nav class="main-nav">
    <a class="active" href="#">Home</a><a href="#">About Us</a><a href="#">Our Services</a><a href="#">Benefits</a><a href="#">Contact Us</a>
  </nav>
</header>

<section class="hero" role="img" aria-label="Photo of a gloved hand steam cleaning tiled floor grout">
  <p class="hero-text">We provides most effective and<br><span class="eco">ecologically friendly</span><br>method of cleaning</p>
</section>

<main class="panel">
  <h1 class="welcome-title">Welcome to Velmora Steam Cleaning</h1>
  <p class="welcome-text">Velmora Steam Cleaning is a business that provides commercial cleaning services utilizing steam vapor, which offers the most effective and ecologically friendly method of cleaning today.</p>

  <div class="steam-banner" role="img" aria-label="Illustration of a steam cleaning machine on green bubbles surrounded by benefit icons">
    <div class="banner-title">Cleaning with steam</div>
    <p class="banner-note" style="left:40px;top:120px">No chemicals or soaps needed</p>
    <p class="banner-note" style="left:650px;top:110px">Cleans, sanitizes, deodorizes and degreases all at the same time</p>
    <p class="banner-note" style="left:70px;top:280px">Safe and eco-friendly green cleaning</p>
    <p class="banner-note" style="left:600px;top:290px">Leaves no residue</p>
  </div>

  <div class="lists">
    <div class="list-col">
      <div class="list-head"><span class="drop"></span>Opportunities</div>
      <ul>
        <li><svg width="14" height="14" viewBox="0 0 14 14"><path d="M2 7l3 3 7-7" fill="none" stroke="#9bcb3c" stroke-width="3"/></svg>Auto Steam Cleaning</li>
        <li><svg width="14" height="14" viewBox="0 0 14 14"><path d="M2 7l3 3 7-7" fill="none" stroke="#9bcb3c" stroke-width="3"/></svg>Carpet Steam Cleaning</li>
        <li><svg width="14" height="14" viewBox="0 0 14 14"><path d="M2 7l3 3 7-7" fill="none" stroke="#9bcb3c" stroke-width="3"/></svg>Industrial Steam Cleaning</li>
        <li><svg width="14" height="14" viewBox="0 0 14 14"><path d="M2 7l3 3 7-7" fill="none" stroke="#9bcb3c" stroke-width="3"/></svg>Furniture</li>
        <li><svg width="14" height="14" viewBox="0 0 14 14"><path d="M2 7l3 3 7-7" fill="none" stroke="#9bcb3c" stroke-width="3"/></svg>Boats of all sizes</li>
        <li><svg width="14" height="14" viewBox="0 0 14 14"><path d="M2 7l3 3 7-7" fill="none" stroke="#9bcb3c" stroke-width="3"/></svg>Awnings, blinds and shutters</li>
        <li><svg width="14" height="14" viewBox="0 0 14 14"><path d="M2 7l3 3 7-7" fill="none" stroke="#9bcb3c" stroke-width="3"/></svg>Cleaning after renovation of buildings</li>
        <li><svg width="14" height="14" viewBox="0 0 14 14"><path d="M2 7l3 3 7-7" fill="none" stroke="#9bcb3c" stroke-width="3"/></svg>Remove bacteria, yeast, molds &amp; fungi</li>
        <li><svg width="14" height="14" viewBox="0 0 14 14"><path d="M2 7l3 3 7-7" fill="none" stroke="#9bcb3c" stroke-width="3"/></svg>Sanitize equipment used for food &amp; beverage</li>
      </ul>
    </div>
    <div class="list-col">
      <div class="list-head"><span class="drop"></span>Benefits</div>
      <ul>
        <li><svg width="14" height="14" viewBox="0 0 14 14"><path d="M2 7l3 3 7-7" fill="none" stroke="#9bcb3c" stroke-width="3"/></svg>Quickly, easily removes dirt, stains &amp; grease</li>
        <li><svg width="14" height="14" viewBox="0 0 14 14"><path d="M2 7l3 3 7-7" fill="none" stroke="#9bcb3c" stroke-width="3"/></svg>Reduce water &amp; chemical consumption</li>
        <li><svg width="14" height="14" viewBox="0 0 14 14"><path d="M2 7l3 3 7-7" fill="none" stroke="#9bcb3c" stroke-width="3"/></svg>Clean hard to reach nooks &amp; crannies</li>
        <li><svg width="14" height="14" viewBox="0 0 14 14"><path d="M2 7l3 3 7-7" fill="none" stroke="#9bcb3c" stroke-width="3"/></svg>Eliminate waste water discrepancy</li>
        <li><svg width="14" height="14" viewBox="0 0 14 14"><path d="M2 7l3 3 7-7" fill="none" stroke="#9bcb3c" stroke-width="3"/></svg>Two operators can clean at once</li>
        <li><svg width="14" height="14" viewBox="0 0 14 14"><path d="M2 7l3 3 7-7" fill="none" stroke="#9bcb3c" stroke-width="3"/></svg>Deodorizes &amp; refreshes surfaces</li>
        <li><svg width="14" height="14" viewBox="0 0 14 14"><path d="M2 7l3 3 7-7" fill="none" stroke="#9bcb3c" stroke-width="3"/></svg>Easy to maintain &amp; operate</li>
        <li><svg width="14" height="14" viewBox="0 0 14 14"><path d="M2 7l3 3 7-7" fill="none" stroke="#9bcb3c" stroke-width="3"/></svg>Continuous, on-demand steam</li>
        <li><svg width="14" height="14" viewBox="0 0 14 14"><path d="M2 7l3 3 7-7" fill="none" stroke="#9bcb3c" stroke-width="3"/></svg>Quick dries without residue</li>
      </ul>
    </div>
  </div>

  <section class="demo">
    <h2 class="demo-title">Check our services<br>demonstrations</h2>
    <p class="demo-text">Watch how our steam machine lifts grease and grime from tile, carpet and steel surfaces in minutes. Each short video shows a real job, step by step, so you can see the results before booking your first visit.</p>
    <div class="video" role="img" aria-label="Video still of a steam cleaning demonstration">
      <svg class="play" width="72" height="52" viewBox="0 0 72 52"><rect width="72" height="52" rx="12" fill="#d33"/><path d="M29 15l18 11-18 11z" fill="#fff"/></svg>
      <div class="video-bar"><span></span></div>
    </div>
  </section>
</main>

<footer class="site-footer">
  <div class="foot-col quick">
    <h3>Quick Links</h3>
    <ul><li>Home</li><li>Benefits</li><li>About Us</li><li>Contact Us</li><li>Our Services</li></ul>
  </div>
  <div class="foot-col contact">
    <h3>Contact Info</h3>
    <p><svg width="12" height="16" viewBox="0 0 12 16"><path d="M6 0a6 6 0 0 0-6 6c0 4 6 10 6 10s6-6 6-10a6 6 0 0 0-6-6zm0 8a2 2 0 1 1 0-4 2 2 0 0 1 0 4z" fill="#fff"/></svg>18 Harbor Lane, Suite 4, Riverton, PR 00960</p>
    <p class="phone"><svg width="14" height="14" viewBox="0 0 14 14"><path d="M3 1l3 3-2 2c1 2 2 3 4 4l2-2 3 3-2 2C6 13 1 8 1 3z" fill="#fff"/></svg>123 456 7890</p>
    <p><svg width="14" height="10" viewBox="0 0 14 10"><rect x=".5" y=".5" width="13" height="9" fill="none" stroke="#fff"/><path d="M.5.5l6.5 5 6.5-5" fill="none" stroke="#fff"/></svg>info@velmorasteam.com</p>
  </div>
  <div class="foot-brand"><span class="brand-dot"></span><span>Velmora<br>Steam Cleaning</span></div>
  <div class="socials"><i></i><i></i><i></i></div>
  <div class="copy-bar"><p class="copy">Copyright 2013 Velmora Steam Cleaning. All Rights Reserved.</p></div>
</footer>
</body>
</html>
```